Medical Practice Business Card

we need a business card for our new medical ophthalmology practice based in Needham Massachusetts. we are looking for a simple , modern and elegant design.
the card needs to contain the following
1- the logo of our practice (please see attached file)
2- the name of the practice : "Silver Birch Retina Care"
3- Doctor's Name: Tobias Rendell MD PhD
4- Specialty: Board-Certified Vitreoretinal Surgeon
5- practice address: 87 Larkspur Ave, Suite 210, Needham MA 02481
7- Office number: 617- 482 - 7730
8- fax number: 617- 391 - 2268
9- email: info@sbretinahub.example
10- website: www.sbretinahub.example

```html
<!DOCTYPE html>
<html lang="en">
<head>
<meta charset="utf-8">
<title>Silver Birch Retina Care – Business Card</title>
<link rel="stylesheet" href="https://fonts.googleapis.com/css2?family=Josefin+Sans:wght@400;600;700&display=swap">
<style>
  :root {
    --navy: #1b3a5f;
    --sky: #7fcbe4;
    --ink: #1f2530;
    --paper: #ffffff;
    --backdrop: #eceff3;
    --edge: #d9dee5;
  }
  * { box-sizing: border-box; margin: 0; padding: 0; }
  html, body {
    width: 1198px; height: 1200px; overflow: hidden;
    background: var(--backdrop);
    font-family: "Josefin Sans", sans-serif;
  }
  .stage { position: relative; width: 1198px; height: 1200px; }
  .card {
    position: absolute; left: 167px; width: 861px; height: 509px;
    background: var(--paper); border: 1px solid var(--edge); overflow: hidden;
  }
  .card--front { top: 74px; }
  .card--back { top: 624px; }

  .name-tab {
    position: absolute; left: 403px; right: 0; top: 74px; height: 48px;
    background: var(--navy); border-radius: 24px 0 0 24px;
    display: flex; align-items: center; padding-left: 38px; gap: 10px;
  }
  .name-tab__name { color: var(--sky); font-weight: 700; font-size: 26px; letter-spacing: 1px; padding-top: 4px; }
  .name-tab__title { color: #fff; font-weight: 400; font-size: 19px; letter-spacing: 1px; padding-top: 4px; }

  .specialty {
    position: absolute; right: 105px; top: 136px;
    color: var(--navy); font-size: 17px; font-weight: 400; letter-spacing: 0.5px;
    white-space: nowrap;
  }

  .brand {
    position: absolute; display: flex; align-items: center;
    color: var(--navy); font-weight: 600; text-transform: uppercase;
    line-height: 1.05; letter-spacing: 1px;
  }
  .brand__dot { flex: none; border-radius: 50%; background: var(--sky); }
  .brand--front { left: 70px; top: 200px; gap: 16px; font-size: 36px; }
  .brand--front .brand__dot { width: 18px; height: 18px; }
  .brand--back { left: 0; right: 0; top: 192px; justify-content: center; gap: 22px; font-size: 56px; }
  .brand--back .brand__dot { width: 26px; height: 26px; }

  .contact { position: absolute; right: 105px; top: 0; color: var(--ink); font-size: 21px; }
  .contact__line { position: absolute; right: 0; white-space: nowrap; }

  .icon-rail {
    position: absolute; left: 772px; top: 238px; width: 38px; bottom: 0;
    background: var(--navy); border-radius: 19px 19px 0 0;
  }
  .icon-rail svg { position: absolute; left: 10px; width: 18px; height: 18px; }
</style>
</head>
<body>
<div class="stage">
  <section class="card card--front">
    <div class="name-tab">
      <span class="name-tab__name">TOBIAS RENDELL</span>
      <span class="name-tab__title">MD PHD</span>
    </div>
    <p class="specialty">Board-Certified Vitreoretinal Surgeon</p>

    <div class="brand brand--front">
      <span class="brand__dot"></span>
      <span>Silver Birch<br>Retina Care</span>
    </div>

    <div class="contact">
      <span class="contact__line" style="top:256px;">617-482-7730</span>
      <span class="contact__line" style="top:289px;">617-391-2268</span>
      <span class="contact__line" style="top:322px;">info@sbretinahub.example</span>
      <span class="contact__line" style="top:356px;">www.sbretinahub.example</span>
      <span class="contact__line" style="top:436px;">87 Larkspur Ave, Suite 210, Needham MA 02481</span>
    </div>

    <div class="icon-rail">
      <svg viewBox="0 0 24 24" style="top:21px" fill="#fff" aria-hidden="true"><path d="M6.6 10.8a15 15 0 0 0 6.6 6.6l2.2-2.2c.3-.3.7-.4 1-.2 1.1.4 2.3.6 3.6.6.6 0 1 .4 1 1V20c0 .6-.4 1-1 1A17 17 0 0 1 3 4c0-.6.4-1 1-1h3.5c.6 0 1 .4 1 1 0 1.3.2 2.5.6 3.6.1.3 0 .7-.2 1z"/></svg>
      <svg viewBox="0 0 24 24" style="top:54px" fill="#fff" aria-hidden="true"><path d="M6 3h12v5H6zM4 9h16a2 2 0 0 1 2 2v6h-4v4H6v-4H2v-6a2 2 0 0 1 2-2zm4 7v3h8v-3z"/></svg>
      <svg viewBox="0 0 24 24" style="top:87px" fill="#fff" aria-hidden="true"><path d="M3 5h18v14H3zm2 2v.5l7 5 7-5V7zm0 3v7h14v-7l-7 5z"/></svg>
      <svg viewBox="0 0 24 24" style="top:120px" fill="none" stroke="#fff" stroke-width="2" aria-hidden="true"><circle cx="12" cy="12" r="9"/><path d="M3 12h18M12 3c3 3 3 15 0 18M12 3c-3 3-3 15 0 18"/></svg>
      <svg viewBox="0 0 24 24" style="top:200px" fill="#fff" aria-hidden="true"><path d="M12 2a7 7 0 0 0-7 7c0 5 7 13 7 13s7-8 7-13a7 7 0 0 0-7-7zm0 9.5A2.5 2.5 0 1 1 12 6.5a2.5 2.5 0 0 1 0 5z"/></svg>
    </div>
  </section>

  <section class="card card--back">
    <div class="brand brand--back">
      <span class="brand__dot"></span>
      <span>Silver Birch<br>Retina Care</span>
    </div>
  </section>
</div>
</body>
</html>
```